"Paint every hour" App Design

Project goal is android app design. "Paint every hour" app is advising about using colors in everyday life to achieve goals, improve life, health, partnership, business and life overall. It is personalized to individual users. Recommendations are provided for personal and business environment, clothes, food etc. It is useful and fun.

Preferred design is clean, neat but special in a way to attract.

The app is functionally finished and ready for publishing. User will color a star/hexagram. This aspect (star) of the app is not subject of design and will remain the same. We are looking for design of all other pieces of the app, buttons, icons, font, icon, etc.

Hi! Based on the feedback we increased the budget. Please reconsider your response. Kind regards

```html
<!DOCTYPE html>
<html lang="en">
<head>
<meta charset="utf-8">
<title>Paint every hour – App Screens</title>
<link rel="stylesheet" href="https://fonts.googleapis.com/css2?family=Quicksand:wght@300;500;700&family=Open+Sans:wght@400;600&display=swap">
<style>
  :root {
    --ink-white: #ffffff;
    --magenta: #ff1fe0;
    --green-text: #1f6a14;
    --purple-text: #8d66a0;
    --panel-white: #f7f7f7;
  }
  * { box-sizing: border-box; margin: 0; padding: 0; }
  html, body { width: 1200px; height: 675px; overflow: hidden; background: #2a2030; }
  .canvas { position: relative; width: 1200px; height: 675px; overflow: hidden; font-family: "Open Sans", sans-serif; }
  .screen { position: absolute; top: 0; height: 675px; overflow: hidden; }

  /* ---------- Screen 1: goals ---------- */
  .screen-goals {
    left: 0; width: 395px;
    background:
      radial-gradient(ellipse at 10% 30%, rgba(60,110,140,.55), transparent 55%),
      radial-gradient(ellipse at 80% 10%, rgba(170,80,110,.5), transparent 60%),
      linear-gradient(180deg, #8a4c78 0%, #6c4a74 55%, #4b3a6a 100%);
  }
  .title { position: absolute; left: 0; right: 0; text-align: center; color: var(--ink-white); font-family: "Quicksand", sans-serif; font-weight: 300; }
  .title-line { letter-spacing: 1px; }
  .title-word { letter-spacing: 8px; padding-left: 8px; }
  .screen-goals .title-line { font-size: 20px; line-height: 24px; }
  .screen-goals .title-word { font-size: 26px; line-height: 32px; }

  .goal { position: absolute; width: 76px; text-align: center; }
  .goal-disc { width: 76px; height: 76px; border-radius: 50%; box-shadow: 0 3px 8px rgba(0,0,0,.25); }
  .goal-label { margin-top: 4px; color: var(--ink-white); font-size: 13px; font-weight: 600; white-space: nowrap; margin-left: -20px; margin-right: -20px; }
  .disc-relationship { background: linear-gradient(90deg, #d15acb 50%, #bb45b6 50%); }
  .disc-goals { background: linear-gradient(90deg, #e8483e 50%, #d63a3a 50%); }
  .disc-improve { background: linear-gradient(90deg, #3fbcba 50%, #2fa6a8 50%); }
  .disc-love { background: linear-gradient(90deg, #ee3a4e 50%, #d82b40 50%); }
  .disc-health { background: linear-gradient(90deg, #55c150 50%, #43ad42 50%); }
  .disc-business { background: linear-gradient(90deg, #4669bd 50%, #3858a8 50%); }

  .to-achieve {
    position: absolute; left: 132px; top: 263px; width: 140px; text-align: center;
    font-family: "Quicksand", sans-serif; font-weight: 300; color: var(--ink-white);
    font-size: 26px; line-height: 27px;
  }
  .start-button {
    position: absolute; left: 145px; top: 510px; width: 110px; height: 110px; border-radius: 22px;
    background: linear-gradient(160deg, #ff3ff0, #c21ab8);
    box-shadow: 0 0 30px rgba(255,60,230,.6);
    display: flex; align-items: center; justify-content: center;
    font-family: "Quicksand", sans-serif; font-weight: 500; font-size: 20px; letter-spacing: 2px; color: var(--ink-white);
  }

  /* ---------- Screen 2: colouring ---------- */
  .screen-colour {
    left: 395px; width: 381px;
    background: radial-gradient(ellipse at 50% 40%, #f3d8f2 0%, #d8a2d6 45%, #b877b8 100%);
  }
  .star-panel { position: absolute; left: 0; top: 0; width: 381px; height: 330px; background: var(--panel-white); box-shadow: 0 4px 8px rgba(0,0,0,.2); }
  .star-area {
    position: absolute; left: 60px; top: 10px; width: 265px; height: 305px;
    background: radial-gradient(circle at 50% 50%, #ffffff 25%, #e9e3ea 60%, #f7f7f7 75%);
  }
  .help-badge {
    position: absolute; right: 16px; top: 14px; width: 32px; height: 32px; border-radius: 50%;
    background: #a78ab0; color: var(--ink-white); font-size: 18px; font-weight: 600;
    display: flex; align-items: center; justify-content: center;
  }
  .tab { position: absolute; top: 283px; width: 66px; height: 47px; background: linear-gradient(#6b4d78, #4a3356); }
  .tab-undo { left: 0; clip-path: polygon(0 0, 80% 0, 100% 100%, 0 100%); }
  .tab-refresh { right: 0; clip-path: polygon(20% 0, 100% 0, 100% 100%, 0 100%); }
  .tab svg { position: absolute; top: 11px; width: 26px; height: 26px; }
  .tab-undo svg { left: 12px; }
  .tab-refresh svg { right: 12px; }

  .palette { position: absolute; left: 39px; top: 370px; display: grid; grid-template-columns: repeat(5, 47px); column-gap: 16px; row-gap: 14px; }
  .swatch { width: 47px; height: 37px; border: 1px solid rgba(120,80,120,.35); }

  .action-bar { position: absolute; left: 10px; right: 10px; top: 597px; height: 78px; background: linear-gradient(#6a4a7a, #4a3258); border-radius: 10px 10px 0 0; }
  .btn {
    position: absolute; display: flex; align-items: center; justify-content: center;
    font-family: "Quicksand", sans-serif; font-weight: 500; letter-spacing: 1px; border-radius: 8px;
  }
  .btn-past { background: linear-gradient(#7b4e8c, #55336a); color: var(--purple-text); border: 1px solid #9a72ac; }
  .btn-analyse { background: linear-gradient(#52cf3c, #2f9a20); color: var(--green-text); border: 1px solid #7be067; }
  .screen-colour .btn { top: 15px; width: 160px; height: 47px; font-size: 17px; }
  .screen-colour .btn-past { left: 10px; }
  .screen-colour .btn-analyse { left: 194px; }

  /* ---------- Screen 3: app icon ---------- */
  .screen-icon {
    left: 776px; width: 424px;
    background: radial-gradient(ellipse at 50% 35%, #5a3f66 0%, #3a2c44 60%, #2c2234 100%);
  }
  .top-bar { position: absolute; left: 0; top: 0; width: 424px; height: 92px; background: linear-gradient(#4c3556, #3a2944); box-shadow: 0 3px 8px rgba(0,0,0,.4); }
  .screen-icon .btn { top: 16px; height: 59px; font-size: 22px; }
  .screen-icon .btn-past { left: 6px; width: 192px; }
  .screen-icon .btn-analyse { left: 226px; width: 190px; }
  .screen-icon .title-line { font-size: 26px; line-height: 30px; }
  .screen-icon .title-line.small { font-size: 20px; line-height: 26px; }
  .screen-icon .title-word { font-size: 34px; line-height: 44px; }

  .icon-tile {
    position: absolute; left: 75px; top: 262px; width: 269px; height: 269px; border-radius: 40px;
    background: linear-gradient(150deg, #8d5ca8, #4b2d5d);
    box-shadow: 0 10px 24px rgba(0,0,0,.5);
  }
  .icon-face {
    position: absolute; inset: 18px; border-radius: 30px;
    background: radial-gradient(circle at 50% 45%, #5a3470 0%, #2a1b34 70%, #1d1424 100%);
    display: flex; align-items: center; justify-content: center; text-align: center;
    font-family: "Quicksand", sans-serif; font-weight: 700; font-size: 26px; line-height: 32px; color: var(--magenta);
  }
  .icon-reflection {
    position: absolute; left: 75px; top: 545px; width: 269px; height: 130px; border-radius: 40px 40px 0 0;
    background: linear-gradient(rgba(140,90,160,.18), rgba(140,90,160,0));
  }
</style>
</head>
<body>
<div class="canvas">

  <!-- Screen 1: goals -->
  <section class="screen screen-goals">
    <div class="title" style="top:16px">
      <div class="title-line">PAINT EVERY</div>
      <div class="title-word">HOUR</div>
    </div>

    <div class="goal" style="left:70px;top:156px">
      <div class="goal-disc disc-relationship" role="img" aria-label="Relationship icon: two people holding hands"></div>
      <div class="goal-label">Relationship</div>
    </div>
    <div class="goal" style="left:190px;top:122px">
      <div class="goal-disc disc-goals" role="img" aria-label="Goals icon: person inside a target"></div>
      <div class="goal-label">Goals</div>
    </div>
    <div class="goal" style="left:280px;top:211px">
      <div class="goal-disc disc-improve" role="img" aria-label="Improve life icon: person beside a rising bar chart"></div>
      <div class="goal-label">Improve Life</div>
    </div>
    <div class="goal" style="left:35px;top:278px">
      <div class="goal-disc disc-love" role="img" aria-label="Love icon: heart"></div>
      <div class="goal-label">Love</div>
    </div>
    <div class="goal" style="left:120px;top:371px">
      <div class="goal-disc disc-health" role="img" aria-label="Health icon: figure shaped as a leafy tree"></div>
      <div class="goal-label">Health</div>
    </div>
    <div class="goal" style="left:253px;top:333px">
      <div class="goal-disc disc-business" role="img" aria-label="Business icon: house with a dollar coin"></div>
      <div class="goal-label">Business</div>
    </div>

    <div class="to-achieve">TO<br>ACHIEVE</div>

    <div class="start-button">START</div>
  </section>

  <!-- Screen 2: colouring -->
  <section class="screen screen-colour">
    <div class="star-panel">
      <div class="star-area" role="img" aria-label="Colouring star that the user paints segment by segment"></div>
      <div class="help-badge">?</div>
      <div class="tab tab-undo">
        <svg viewBox="0 0 24 24" fill="none" stroke="#ffffff" stroke-width="2" stroke-linecap="round" stroke-linejoin="round"><path d="M9 5 4 10l5 5"/><path d="M4 10h9a6 6 0 0 1 0 12h-2"/></svg>
      </div>
      <div class="tab tab-refresh">
        <svg viewBox="0 0 24 24" fill="none" stroke="#ffffff" stroke-width="2" stroke-linecap="round" stroke-linejoin="round"><path d="M20 7a8 8 0 0 0-14-1"/><path d="M20 3v4h-4"/><path d="M4 17a8 8 0 0 0 14 1"/><path d="M4 21v-4h4"/></svg>
      </div>
    </div>

    <div class="palette">
      <div class="swatch" style="background:#ffffff"></div>
      <div class="swatch" style="background:#e4e4e6"></div>
      <div class="swatch" style="background:#e8c020"></div>
      <div class="swatch" style="background:#7089a0"></div>
      <div class="swatch" style="background:#000000"></div>
      <div class="swatch" style="background:#ffff00"></div>
      <div class="swatch" style="background:#ffa500"></div>
      <div class="swatch" style="background:#ff0000"></div>
      <div class="swatch" style="background:#5c3030"></div>
      <div class="swatch" style="background:#8b0000"></div>
      <div class="swatch" style="background:#d4207a"></div>
      <div class="swatch" style="background:#2b0a6b"></div>
      <div class="swatch" style="background:#650060"></div>
      <div class="swatch" style="background:#87cefa"></div>
      <div class="swatch" style="background:#0000ff"></div>
      <div class="swatch" style="background:#ffffff"></div>
      <div class="swatch" style="background:#40e0d0"></div>
      <div class="swatch" style="background:#55ff00"></div>
      <div class="swatch" style="background:#006400"></div>
      <div class="swatch" style="background:#ffffff"></div>
    </div>

    <div class="action-bar">
      <div class="btn btn-past">PAST STAR</div>
      <div class="btn btn-analyse">ANALYSE</div>
    </div>
  </section>

  <!-- Screen 3: app icon -->
  <section class="screen screen-icon">
    <div class="top-bar">
      <div class="btn btn-past">PAST STAR</div>
      <div class="btn btn-analyse">ANALYSE</div>
    </div>

    <div class="title" style="top:138px">
      <div class="title-line small">APP ICON</div>
      <div class="title-line">PAINT EVERY</div>
      <div class="title-word">HOUR</div>
    </div>

    <div class="icon-tile">
      <div class="icon-face">Paint<br>every hour</div>
    </div>
    <div class="icon-reflection"></div>
  </section>

</div>
</body>
</html>
```